Crooked Meadow Cider - New Cider Label (Plumora Clove Cider)

Crooked Meadow Cider is wanting a can label for our new apple, cinnamon, and rhubarb cider.

Name of Cider: Plumora Clove Cider
Tasting Notes: Rhubarb from grandpa's garden, cinnamon, and apples create an elegant, spicy, and warming cider.
ABV: 8%

We would like the NEW can design to include the "head" logo in some capacity as it represents the founder's wife and four daughters who developed the brand.

Some suggestions are - stems of rhubarb and cinnamon intertwined with the branches coming out of the head of the existing logo, the use of maroon/purple colours to represent the rhubarb and possibly colours to represent the cinnamon.
Or if you have a better idea, please submit that!

Requirements
Must have
• The "head" logo in some capacity as it represents the founder's wife and four daughters who developed the brand.

```html
<!DOCTYPE html>
<html lang="en">
<head>
<meta charset="utf-8">
<title>Crooked Meadow Cider – Plumora Clove Cider Label</title>
<link rel="stylesheet" href="https://fonts.googleapis.com/css2?family=Open+Sans:wght@400;700;800&display=swap">
<style>
  :root {
    --backdrop: #e6e6e8;
    --label: #ffffff;
    --magenta: #b51f8c;
    --violet: #7b2a92;
    --ink: #111111;
    --ink-soft: #222222;
    --ring-grey: #e4e4e4;
  }
  * { margin: 0; padding: 0; box-sizing: border-box; }
  html, body {
    width: 1200px;
    height: 809px;
    overflow: hidden;
    background: var(--backdrop);
  }
  .canvas {
    position: relative;
    width: 1200px;
    height: 809px;
  }
  .can-label {
    position: absolute;
    left: 383px;
    top: 24px;
    width: 434px;
    height: 760px;
    background: var(--label);
    font-family: "Open Sans", Arial, sans-serif;
    overflow: hidden;
  }
  .band {
    position: absolute;
    left: 136px;
    width: 163px;
    background: var(--magenta);
  }
  .band--top { top: 0; height: 86px; border-radius: 0 0 5px 5px; }
  .band--bottom { top: 701px; height: 59px; border-radius: 5px 5px 0 0; }
  .origin-line {
    position: absolute;
    top: 96px;
    left: 0;
    width: 434px;
    text-align: center;
    font-weight: 800;
    font-size: 11.8px;
    line-height: 1;
    letter-spacing: 0.3px;
    color: var(--ink);
    white-space: nowrap;
  }
  .brush-ring {
    position: absolute;
    left: 50px;
    top: 161px;
    width: 312px;
    height: 312px;
  }
  .emblem {
    position: absolute;
    left: 88px;
    top: 199px;
    width: 236px;
    height: 236px;
    border-radius: 50%;
    background: radial-gradient(circle, #ffffff 62%, var(--ring-grey) 100%);
    display: flex;
    align-items: center;
    justify-content: center;
  }
  .emblem__name {
    font-weight: 700;
    font-size: 21px;
    color: var(--ink);
    text-align: center;
    line-height: 1.15;
  }
  .tasting-strip {
    position: absolute;
    left: 412px;
    top: 134px;
    width: 18px;
    height: 528px;
    background: var(--magenta);
    border-radius: 5px;
    display: flex;
    align-items: center;
    justify-content: center;
  }
  .tasting-strip__text {
    writing-mode: vertical-rl;
    font-family: Arial, "Open Sans", sans-serif;
    font-size: 11.8px;
    line-height: 1;
    color: #ffffff;
    white-space: nowrap;
  }
  .variety {
    position: absolute;
    top: 534px;
    left: 0;
    width: 434px;
    text-align: center;
    font-weight: 800;
    font-size: 25px;
    line-height: 1;
    letter-spacing: 0.8px;
    color: var(--ink);
    white-space: nowrap;
  }
  .style-name {
    position: absolute;
    top: 558px;
    left: 0;
    width: 434px;
    padding-left: 14px;
    text-align: center;
    font-weight: 800;
    font-size: 64px;
    line-height: 1;
    letter-spacing: 14px;
    color: var(--magenta);
    white-space: nowrap;
  }
  .abv__value,
  .abv__unit {
    position: absolute;
    left: 0;
    width: 434px;
    text-align: center;
    font-family: Arial, "Open Sans", sans-serif;
    line-height: 1;
  }
  .abv__value { top: 645px; font-size: 32px; color: var(--violet); }
  .abv__unit { top: 675px; font-size: 22px; color: var(--ink-soft); }
</style>
</head>
<body>
<main class="canvas">
  <section class="can-label">
    <div class="band band--top"></div>
    <p class="origin-line">100% AUSTRALIAN APPLES</p>

    <svg class="brush-ring" viewBox="0 0 312 312" role="img" aria-label="Magenta and purple brush-stroke ring framing the brand emblem">
      <defs>
        <linearGradient id="ringTone" x1="0" y1="0" x2="1" y2="1">
          <stop offset="0" stop-color="#b51f8c"/>
          <stop offset="1" stop-color="#7b2a92"/>
        </linearGradient>
      </defs>
      <circle cx="156" cy="156" r="156" fill="url(#ringTone)"/>
    </svg>

    <div class="emblem">
      <p class="emblem__name">Crooked Meadow</p>
    </div>

    <div class="tasting-strip">
      <p class="tasting-strip__text">Rhubarb from grandpa's garden, cinnamon, and apples create an elegant, spicy, and warming cider.</p>
    </div>

    <h1 class="variety">PLUMORA CLOVE</h1>
    <p class="style-name">CIDER</p>

    <p class="abv"><span class="abv__value">8%</span><span class="abv__unit">ABV</span></p>

    <div class="band band--bottom"></div>
  </section>
</main>
</body>
</html>
```